Larkfield Circuitry LLC is a Minneapolis / St Paul and surrounding communities computer repair and service company. It serves residential and small businesses. We work primarily with virus removal, data recovery, system baselines, networking, and new system installation. The site should look clean, professional, and easy to navigate.

This wordpress project must be coded and integrated into a wordpress theme for easy upload and maintenance.
Updates

Designers - Please make sure your design is in a wordpress theme so that It can be uploaded.  

Thank you,

Brin 

Target Market(s)

Residential and Small Business

Industry/Entity Type

Residential

Requirements
Must have
• Site Content
1. Main Page should have photos that scroll across, Business Description, Space to run
“Specials” Ads
a. Intuitive Navigation
2. Additional Pages
a. Blog for Computer Repair Articles
b. Testimonials Page
c. Contact Pages
d. Services Page with the ability to put in pricing
3. The site must be clean and professional.
4. Wordpress Theme

```html
<!DOCTYPE html>
<html lang="en">
<head>
<meta charset="utf-8">
<title>Larkfield Circuitry LLC – Technical Support</title>
<link href="https://fonts.googleapis.com/css2?family=Advent+Pro:wght@500;600&family=Arimo:wght@400;700&family=Ubuntu:wght@500;700&display=swap" rel="stylesheet">
<style>
  :root{
    --page-bg:#ededed;
    --page-bg-edge:#e2e2e2;
    --ink:#4a4a4a;
    --ink-dark:#222;
    --green:#4f9a23;
    --green-light:#6cbf2e;
    --green-dark:#3d7d19;
    --bar:#262626;
    --bar-edge:#161616;
    --hero:#1c1c1c;
    --row-light:#ececec;
    --row-dark:#d9d9d9;
    --white:#fff;
  }
  *{box-sizing:border-box;margin:0;padding:0}
  html,body{width:1200px;height:719px;overflow:hidden}
  body{background:radial-gradient(ellipse at 50% 40%,var(--page-bg) 0%,var(--page-bg-edge) 100%);font-family:"Arimo",Arial,sans-serif;color:var(--ink)}
  .canvas{position:relative;width:1200px;height:719px;overflow:hidden;border-top:3px solid #3a3a3a}

  /* header */
  .brand{position:absolute;left:176px;top:17px;display:flex;align-items:center;gap:10px}
  .brand-mark{width:66px;height:66px;border-radius:50%;border:5px solid var(--green);background:var(--white)}
  .brand-name{font-family:"Ubuntu",sans-serif;font-weight:700;font-size:24px;color:var(--ink);letter-spacing:.2px}
  .phone{position:absolute;left:754px;top:34px;display:flex;align-items:center;gap:8px;font-family:"Arimo",sans-serif;font-weight:700;font-size:22px;color:var(--ink-dark);letter-spacing:.5px}
  .phone-icon{width:24px;height:24px}
  .mascot{position:absolute;left:955px;top:0;width:70px;height:107px;border-radius:0 0 6px 6px;background:linear-gradient(180deg,#f0d2b4 0%,#9fc2e6 55%,#e6e6e6 100%)}

  /* navigation */
  .main-nav{position:absolute;left:176px;top:107px;width:848px;height:33px;background:linear-gradient(#333,var(--bar-edge));border-radius:3px;display:flex;font-family:"Advent Pro",sans-serif;font-weight:600;font-size:14px}
  .main-nav a{color:#eee;text-decoration:none;padding:0 20px;line-height:33px;position:relative}
  .main-nav a+a::before{content:"";position:absolute;left:0;top:10px;height:13px;border-left:1px solid #555}
  .main-nav a.current{background:linear-gradient(var(--green-light),var(--green));border-radius:3px 0 0 3px;padding:0 18px}

  /* side decoration */
  .devices-art{position:absolute;left:0;top:78px;width:176px;height:250px;background:radial-gradient(ellipse at 45% 50%,#d6d6d6 0%,rgba(230,230,230,0) 70%)}

  /* hero */
  .hero{position:absolute;left:176px;top:158px;width:848px;height:294px;background:radial-gradient(ellipse at 55% 60%,#2e2e2e 0%,var(--hero) 75%);border-radius:4px}
  .hero-title{position:absolute;left:32px;top:36px;font-family:"Arimo",sans-serif;font-weight:400;font-size:49px;color:var(--white);letter-spacing:-.5px}
  .hero-title span{color:var(--green)}
  .hero-tagline{position:absolute;left:366px;top:91px;font-size:12px;color:var(--white)}
  .hero-copy{position:absolute;left:33px;top:120px;width:545px;font-family:"Advent Pro",sans-serif;font-weight:500;font-size:11.5px;line-height:19px;color:var(--green-light)}
  .hero-cta{position:absolute;left:33px;top:192px;display:flex;align-items:center;gap:11px}
  .btn-light{display:inline-block;width:86px;height:27px;line-height:27px;text-align:center;font-size:12px;color:#222;background:linear-gradient(#fff,#cfcfcf);border-radius:4px}
  .hero-cta strong{font-size:14.5px;color:var(--white)}
  .slider-dots{position:absolute;left:33px;top:278px;display:flex;gap:5px}
  .slider-dots i{width:8px;height:8px;border-radius:50%;background:#ddd}
  .slider-dots i.active{background:var(--green-light)}
  .monitor-art{position:absolute;left:806px;top:120px;width:145px;height:377px;border-radius:8px;background:linear-gradient(160deg,#555 0%,#111 45%,#000 100%)}

  /* social tab */
  .social-tab{position:absolute;left:1157px;top:88px;width:43px;height:135px;background:var(--green);border-radius:5px 0 0 5px;display:flex;flex-direction:column;align-items:center;gap:5px;padding-top:12px}
  .social-tab a{width:24px;height:24px;border-radius:3px;background:#f4f4f4;display:block}

  /* services */
  .services{position:absolute;left:176px;top:501px;width:848px;display:grid;grid-template-columns:repeat(5,1fr);border-radius:4px 4px 0 0;overflow:hidden}
  .service{display:flex;flex-direction:column}
  .service h2{height:48px;background:linear-gradient(#2c2c2c,var(--bar-edge));color:var(--white);font-family:"Ubuntu",sans-serif;font-weight:700;font-size:13px;letter-spacing:.3px;display:flex;align-items:center;gap:8px;padding-left:9px}
  .service h2::before{content:"";width:13px;height:13px;border-radius:50%;background:var(--green-light);box-shadow:inset 0 0 0 3px var(--green-dark)}
  .service ul{list-style:none}
  .service li{height:30.5px;line-height:30.5px;font-size:11.5px;color:#222;padding-left:26px;position:relative;border-bottom:1px solid #f7f7f7;background:var(--row-light)}
  .service li:nth-child(even){background:var(--row-dark)}
  .service li::before{content:"";position:absolute;left:9px;top:10px;width:10px;height:10px;border-radius:50%;background:#7fb25a}
  .service li::after{content:"";position:absolute;left:13px;top:13px;border-left:4px solid #fff;border-top:2px solid transparent;border-bottom:2px solid transparent}
  .service .more{background:var(--row-dark);height:38px;padding:7px 0 0 9px}
  .btn-green{display:inline-block;height:21px;line-height:21px;padding:0 8px;font-size:11px;color:var(--white);background:linear-gradient(var(--green-light),var(--green-dark));border-radius:2px}
  .service+.service{border-left:1px solid #c8c8c8}
</style>
</head>
<body>
<div class="canvas">
  <header>
    <div class="brand">
      <div class="brand-mark"></div>
      <span class="brand-name">Larkfield Circuitry LLC</span>
    </div>
    <div class="phone">
      <svg class="phone-icon" viewBox="0 0 24 24" aria-hidden="true">
        <circle cx="12" cy="12" r="12" fill="#5aa82a"/>
        <path d="M7 9c0-2 2-3 5-3s5 1 5 3v1h-3V9h-4v1H7z M8 12h8l1 6H7z" fill="#fff"/>
      </svg>
      +01 5550 2841
    </div>
    <div class="mascot" role="img" aria-label="Illustration of a support technician working at a laptop"></div>
  </header>

  <nav class="main-nav">
    <a class="current" href="#">Home</a>
    <a href="#">About Us</a>
    <a href="#">Blog</a>
    <a href="#">Services</a>
    <a href="#">Testimonials</a>
    <a href="#">Contact</a>
  </nav>

  <div class="devices-art" role="img" aria-label="Computer tower and laptop with floating paper sheets"></div>

  <section class="hero">
    <h1 class="hero-title">Technical <span>SUPPORT</span></h1>
    <p class="hero-tagline">ANY TIME, ANY WHERE</p>
    <p class="hero-copy">Lorem Ipsum is simply dummy text of the printing and typesetting industry. Lorem Ipsum is simply Lorem Ipsum is simply dummy text of the printing and typesetting industry. Lorem Ipsum is simply dummy text of the printing and typesetting industry..</p>
    <div class="hero-cta">
      <a class="btn-light">Learn More</a>
      <strong>Offering Execellent</strong>
    </div>
    <div class="slider-dots"><i></i><i class="active"></i><i></i><i></i><i></i></div>
  </section>
  <div class="monitor-art" role="img" aria-label="Black flat-screen monitor with keyboard"></div>

  <aside class="social-tab" aria-label="Social links">
    <a href="#"></a><a href="#"></a><a href="#"></a><a href="#"></a>
  </aside>

  <section class="services">
    <article class="service">
      <h2>VIRUS REMOVAL</h2>
      <ul><li>Lorem Ipsum new data</li><li>$50 Ipsum new data</li><li>Lorem Ipsum new data</li><li>Lorem Ipsum new data</li></ul>
      <div class="more"><a class="btn-green">Learn More</a></div>
    </article>
    <article class="service">
      <h2>DATA RECOVERY</h2>
      <ul><li>Lorem Ipsum new data</li><li>$100 Ipsum new data</li><li>Lorem Ipsum new data</li><li>Lorem Ipsum new data</li></ul>
      <div class="more"><a class="btn-green">Learn More</a></div>
    </article>
    <article class="service">
      <h2>SYSTEM BASELINES</h2>
      <ul><li>Lorem Ipsum new data</li><li>$250 Ipsum new data</li><li>Lorem Ipsum new data</li><li>Lorem Ipsum new data</li></ul>
      <div class="more"><a class="btn-green">Learn More</a></div>
    </article>
    <article class="service">
      <h2>NETWORKING</h2>
      <ul><li>Lorem Ipsum new data</li><li>$85 sum new data</li><li>Lorem Ipsum new data</li><li>Lorem Ipsum new data</li></ul>
      <div class="more"><a class="btn-green">Learn More</a></div>
    </article>
    <article class="service">
      <h2>INSTALLATION</h2>
      <ul><li>Lorem Ipsum new data</li><li>$110 Ipsum new data</li><li>Lorem Ipsum new data</li><li>Lorem Ipsum new data</li></ul>
      <div class="more"><a class="btn-green">Learn More</a></div>
    </article>
  </section>
</div>
</body>
</html>
```